Roll-Up Banner für Glückswebsite
Das war eine großartige Zusammenarbeit und unserem sehr knappen Zeitplan extrem entgegenkommend. Das design ist gleichzeitig seriös und trotzdem jung und dynamisch! Perfekt!
Zielgruppe
Die Website, www.freudenpfad.de ermöglicht es jedem Interessierten kostenlos mehr über das eigene Lebensglück, persönliche Stärken, und die eigene Lebenszufriedenheit herauszufinden. Interessierte können online Fragebögen ausfüllen, und erhalten neben einer detaillierten Rückmeldung über die eigenen Möglichkeiten und Stärken, Hinweise dazu, wie Sie an Ihrem eigenen Potenzial arbeiten können. Es handelt sich um ein Kooperationsprojekt der Nordischen Vereinigung für Heitere Seelenkunde der Uni Wendelstein, der HK-Lindau, der Health Academy Marbach und der Uni Falkenried. Zielgruppe für das Banner sind Menschen, die selbst mit Klienten im Kontext der Positiven Psychologie arbeiten oder Menschen, die sich Ihrem eigenen Lebensglück zuwenden wollen.
Aufgabenstellung
Es handelt sich um ein Roll-up Banner in den Maßen 1m Breite und 2 Meter Höhe.
Das Banner sollte so angelegt sein, dass es interessierten Besuchern auf Kongressen vermittelt, was es mit der Seite Freudenpfad.de auf sich hat. Also wissenschaftlich evaluierte kostenfreie online-Fragebögen, die Menschen dabei helfen Ihre eigenen Stärken und Potenziale zu entdecken und dem eigenen Glück näher zu kommen.
Es sollte außerdem das Logo der NVHS darauf zu sehen sein, sowie kleiner die Logos der Forschungskooperationspartner, HK-Lindau, Uni Wendelstein, Uni Falkenried, Health Academy Marbach.
Die Farben sollten zum Logo der NVHS passen.

```html
<!DOCTYPE html>
<html lang="de">
<head>
<meta charset="utf-8">
<title>Roll-Up Banner – Freudenpfad.de</title>
<link href="https://fonts.googleapis.com/css2?family=Ubuntu:wght@400;500;700&display=swap" rel="stylesheet">
<style>
  :root{
    --navy:#1d3a6e;
    --navy-deep:#0f2a5c;
    --teal:#2aa5b8;
    --teal-soft:#4fb5b3;
    --green:#5fab48;
    --paper:#f5f6f8;
    --footer:#e4e6ea;
    --stage:#c9ccd3;
    --photo-a:#c9c6c2;
    --photo-b:#9c9894;
    --step1:#76c3d6;
    --step2:#229a93;
    --step3:#2c9863;
    --step4:#1d3a6e;
  }
  *{box-sizing:border-box;margin:0;padding:0}
  html,body{width:768px;height:1200px;overflow:hidden}
  body{background:var(--stage);font-family:"Ubuntu",sans-serif;color:var(--navy)}
  .banner{position:absolute;left:89px;top:20px;width:590px;height:1160px;background:var(--paper);overflow:hidden}
  .header{position:absolute;left:0;top:0;width:100%;height:168px}
  .brand{position:absolute;left:48px;top:96px;display:flex;flex-direction:column}
  .brand-name{font-size:22px;font-weight:700;letter-spacing:2px;color:var(--navy)}
  .brand-sub{font-size:7.5px;font-weight:500;line-height:10px;margin-top:6px;color:var(--navy)}
  .url-band{position:absolute;left:0;top:168px;width:100%;height:48px;
    background:linear-gradient(90deg,#55b5b3,#2aa6c2);display:flex;align-items:center;justify-content:center}
  .url-band span{font-size:33px;font-weight:400;color:var(--navy);letter-spacing:-.3px}
  .portraits{position:absolute;left:0;top:216px;width:100%;height:224px;display:grid;
    grid-template-columns:repeat(5,1fr);grid-template-rows:114px 110px;gap:2px;background:#ddd}
  .portrait{background:linear-gradient(160deg,var(--photo-a),var(--photo-b))}
  .portrait.warm{background:linear-gradient(180deg,#cfcbc6 0%,#a9a39c 75%,#d6a43a 100%)}
  .portrait.cool{background:linear-gradient(180deg,#cdcac6 0%,#a19d98 75%,#4f8fc7 100%)}
  .content{position:absolute;left:0;top:440px;width:100%;height:573px;
    background:
      linear-gradient(180deg,rgba(0,0,0,0) 40%,rgba(95,171,72,.55) 100%),
      linear-gradient(120deg,#58b1a0 0%,#2fa0ae 100%)}
  .lead{position:absolute;left:45px;top:40px;font-size:16.5px;font-weight:700;color:var(--navy-deep);letter-spacing:-.2px}
  .intro{position:absolute;left:45px;top:78px;width:510px;font-size:16.5px;line-height:22px;color:var(--navy)}
  .steps{position:absolute;left:0;top:0;width:100%;height:100%}
  .timeline{position:absolute;left:60px;top:207px;width:2px;height:230px;background:#e9f3f0}
  .step{position:absolute;left:0;width:100%}
  .dot{position:absolute;left:48px;width:27px;height:27px;border-radius:50%;border:2px solid #fff}
  .step-title{position:absolute;left:93px;font-size:23px;color:var(--navy);white-space:nowrap}
  .step-note{position:absolute;left:93px;font-size:16px;color:var(--navy);white-space:nowrap}
  .badge{position:absolute;left:406px;top:276px;width:186px;height:54px;background:var(--navy-deep);
    transform:rotate(-2deg);color:#fff;font-size:12.5px;line-height:16px;text-align:center;
    display:flex;flex-direction:column;justify-content:center}
  .rule{position:absolute;left:0;top:1013px;width:100%;height:6px;background:var(--navy-deep)}
  .footer{position:absolute;left:0;top:1019px;width:100%;height:141px;background:var(--footer)}
  .footer-title{position:absolute;left:45px;top:22px;font-size:17px;color:var(--navy)}
  .partners{position:absolute;left:45px;right:45px;top:72px;display:flex;justify-content:space-between;align-items:center}
  .partner{display:flex;align-items:center;gap:5px;font-size:10px;font-weight:500;color:var(--navy)}
  .partner i{width:14px;height:14px;border-radius:50%;background:var(--navy);display:block}
</style>
</head>
<body>
<div class="banner">
  <header class="header">
    <div class="brand">
      <span class="brand-name">NVHS</span>
      <span class="brand-sub">Nordische Vereinigung für<br>Heitere Seelenkunde</span>
    </div>
  </header>

  <div class="url-band"><span>www.freudenpfad.de</span></div>

  <div class="portraits">
    <div class="portrait warm" role="img" aria-label="Porträtfoto: lachender junger Mann"></div>
    <div class="portrait cool" role="img" aria-label="Porträtfoto: lächelnde junge Frau"></div>
    <div class="portrait warm" role="img" aria-label="Porträtfoto: Mann mit Brille und Bart"></div>
    <div class="portrait" role="img" aria-label="Porträtfoto: ältere Dame"></div>
    <div class="portrait cool" role="img" aria-label="Porträtfoto: lachender junger Mann mit Brille"></div>
    <div class="portrait" role="img" aria-label="Porträtfoto: lächelnde Frau"></div>
    <div class="portrait warm" role="img" aria-label="Porträtfoto: lachender Mann"></div>
    <div class="portrait cool" role="img" aria-label="Porträtfoto: ältere Frau mit Brille"></div>
    <div class="portrait cool" role="img" aria-label="Porträtfoto: lächelnder Mann"></div>
    <div class="portrait" role="img" aria-label="Porträtfoto: lachende junge Frau"></div>
  </div>

  <section class="content">
    <p class="lead">Wollen Sie mehr über sich und Ihre Stärken erfahren?</p>
    <p class="intro">Unter www.freudenpfad.de haben Sie die Möglichkeit kostenfrei die neusten wissenschaftlichen Fragebögen im Bereich der Positiven Psychologie zu nutzen und ein detailliertes Feedback zu Ihren Ergebnissen zu erhalten.</p>

    <div class="steps">
      <div class="timeline"></div>
      <div class="step" style="top:194px">
        <span class="dot" style="background:var(--step1)"></span>
        <span class="step-title" style="top:-2px">Persönliches Konto einrichten</span>
        <span class="step-note" style="top:32px">– und damit immer Zugriff auf Ihre Ergebnisse haben</span>
      </div>
      <div class="step" style="top:280px">
        <span class="dot" style="background:var(--step2)"></span>
        <span class="step-title" style="top:-2px">Online-Fragebogen ausfüllen</span>
        <span class="step-note" style="top:32px">unter www.freudenpfad.de</span>
      </div>
      <div class="badge"><span>wissenschaftlich evaluiert</span><span>kostenfrei | anonym</span></div>
      <div class="step" style="top:367px">
        <span class="dot" style="background:var(--step3)"></span>
        <span class="step-title" style="top:-2px">Persönliche Rückmeldung erhalten</span>
      </div>
      <div class="step" style="top:424px">
        <span class="dot" style="background:var(--step4)"></span>
        <span class="step-title" style="top:-2px">Ein noch erfüllteres Leben gestalten</span>
        <span class="step-note" style="top:26px">– mit unseren Hinweisen</span>
      </div>
    </div>
  </section>

  <div class="rule"></div>

  <footer class="footer">
    <p class="footer-title">Forschungskooperationspartner</p>
    <div class="partners">
      <span class="partner"><i></i>Uni Wendelstein</span>
      <span class="partner">Health Academy Marbach</span>
      <span class="partner"><i></i>HK-Lindau</span>
      <span class="partner"><i></i>Uni Falkenried</span>
    </div>
  </footer>
</div>
</body>
</html>
```